Cell phone repair

you can please design me business card

size 3.5" x 2"

colors blue and red

fixit rapid logo (you get from my website fixitrapidco.example )

"We Come To You!

It is very simple! You tell us what phone you have, And we come to fix it."

phone number: 555.248.3906

website: www.fixitrapidco.example

email: info@fixitrapidco.example

```html
<!DOCTYPE html>
<html lang="en">
<head>
<meta charset="UTF-8">
<title>Fixit Rapid – Business Card</title>
<link rel="stylesheet" href="https://fonts.googleapis.com/css2?family=Work+Sans:wght@400;500&display=swap">
<style>
  :root {
    --sky: #5ccbf1;
    --sky-deep: #3fbfea;
    --red: #ec1c2a;
    --white: #ffffff;
    --backdrop: #2e2c2a;
  }
  * { margin: 0; padding: 0; box-sizing: border-box; }
  html, body {
    width: 800px; height: 1200px; overflow: hidden;
    background: var(--backdrop);
    font-family: "Work Sans", sans-serif;
  }
  .card {
    position: absolute; left: 80px;
    width: 640px; height: 366px;
    border-radius: 24px; overflow: hidden;
  }
  .card-front { top: 150px; background: var(--sky); }
  .card-back { top: 684px; background: var(--white); }

  .brand {
    position: absolute; display: flex; align-items: center; gap: 14px;
    font-weight: 500; letter-spacing: -0.5px; white-space: nowrap;
  }
  .brand-dot { border-radius: 50%; flex: none; }

  .card-front .brand {
    left: 50%; top: 50%; transform: translate(-50%, -50%);
    color: var(--white); font-size: 52px;
  }
  .card-front .brand-dot { width: 40px; height: 40px; background: var(--white); }

  .card-back .brand {
    left: 40px; top: 52px; color: var(--sky); font-size: 32px;
  }
  .card-back .brand-dot { width: 26px; height: 26px; background: var(--red); }

  .waves { position: absolute; inset: 0; }

  .holder {
    position: absolute; right: 40px; top: 60px; text-align: right;
  }
  .holder-name {
    color: var(--sky); font-size: 28px; font-weight: 400; letter-spacing: 0.5px;
  }
  .holder-role { color: var(--red); font-size: 16px; margin-top: 2px; }

  .contact {
    position: absolute; right: 30px; bottom: 14px;
    list-style: none; text-align: right; color: var(--white);
    font-size: 13px; line-height: 17px;
  }
  .contact li { display: flex; justify-content: flex-end; align-items: center; gap: 8px; }
  .contact li.plain { padding-right: 20px; }
  .contact svg { width: 12px; height: 12px; flex: none; }
</style>
</head>
<body>

<section class="card card-front">
  <div class="brand"><span class="brand-name">Fixit Rapid</span><span class="brand-dot"></span></div>
</section>

<section class="card card-back">
  <svg class="waves" viewBox="0 0 640 366" preserveAspectRatio="none">
    <path d="M110,220 C220,272 330,272 430,246 C510,226 580,196 640,172 L640,180 C580,204 510,236 430,256 C330,282 220,280 110,220 Z" fill="var(--sky-deep)"/>
    <path d="M0,205 C60,268 200,300 340,275 C440,255 540,215 640,190 L640,366 L0,366 Z" fill="var(--sky)"/>
    <path d="M0,140 C40,215 160,262 360,266 C180,270 50,242 0,190 Z" fill="var(--red)"/>
  </svg>

  <div class="brand"><span class="brand-name">Fixit Rapid</span><span class="brand-dot"></span></div>

  <div class="holder">
    <div class="holder-name">DANIEL BROOKS</div>
    <div class="holder-role">Director</div>
  </div>

  <ul class="contact">
    <li class="plain">418 Maple Ridge Road</li>
    <li class="plain">Lexford, KY 40599</li>
    <li>555.248.3906
      <svg viewBox="0 0 12 12"><path d="M2.5 1h2l1 2.5-1.3 1a6 6 0 0 0 3.3 3.3l1-1.3 2.5 1v2c0 .6-.5 1-1 1A9.5 9.5 0 0 1 1.5 2c0-.5.4-1 1-1z" fill="var(--white)"/></svg>
    </li>
    <li>info@fixitrapidco.example
      <svg viewBox="0 0 12 12"><rect x="1" y="2.5" width="10" height="7" rx="1" fill="none" stroke="var(--white)" stroke-width="1.2"/><path d="M1.5 3l4.5 3.5L10.5 3" fill="none" stroke="var(--white)" stroke-width="1.2"/></svg>
    </li>
    <li>www.fixitrapidco.example
      <svg viewBox="0 0 12 12"><circle cx="6" cy="6" r="5" fill="none" stroke="var(--white)" stroke-width="1.1"/><ellipse cx="6" cy="6" rx="2.2" ry="5" fill="none" stroke="var(--white)" stroke-width="1"/><path d="M1 6h10" stroke="var(--white)" stroke-width="1"/></svg>
    </li>
  </ul>
</section>

</body>
</html>
```